Corvane Skin & Tissue Pathology CPC postcard

Need a postcard advertising our dermatopathology consultative services, and in particular, our new MeetLoop-based online clinico-pathologic correlation service. Would like the postcard to be clean, professional, modern, with great fonts. I have attached a basic draft postcard and my picture. Please use these as a starting point, but feel free to improvise. Please also see our website, www.tissuereviewdesk.example.

Industry/Entity Type

Advertising

```html
<!DOCTYPE html>
<html lang="en">
<head>
<meta charset="utf-8">
<title>Corvane Skin &amp; Tissue Pathology – CPC Postcard</title>
<link rel="stylesheet" href="https://fonts.googleapis.com/css2?family=Open+Sans:wght@400;600;700&family=Arimo:wght@400;700&display=swap">
<style>
  :root {
    --stage: #4a4645;
    --paper: #ffffff;
    --red: #e0231c;
    --ink: #1a1a1a;
    --grey-line: #555555;
    --blush: #f6e9ef;
    --photo-light: #e9e9e9;
    --photo-dark: #8a8a8a;
  }
  * { box-sizing: border-box; margin: 0; padding: 0; }
  html, body {
    width: 806px; height: 1200px; overflow: hidden;
    background: var(--stage);
    font-family: "Open Sans", Arial, sans-serif;
    color: var(--ink);
  }
  .card {
    position: absolute; left: 40px; width: 722px;
    background: var(--paper); overflow: hidden;
  }
  .card--front { top: 22px; height: 554px;
    background: linear-gradient(120deg, #ffffff 0%, var(--blush) 45%, #ffffff 80%); }
  .card--back { top: 610px; height: 554px; }

  .front-art { position: absolute; inset: 0; }
  .brand-front {
    position: absolute; left: 30px; top: 62px;
    font-size: 14px; font-weight: 600; color: var(--red);
    display: flex; align-items: center; gap: 8px; letter-spacing: .02em;
  }
  .brand-front .dot { width: 12px; height: 12px; border-radius: 50%; background: var(--red); }
  .service-title {
    position: absolute; left: 29px; top: 150px;
    font-size: 29px; line-height: 35px; font-weight: 400; color: var(--red);
  }
  .tagline {
    position: absolute; left: 29px; top: 276px;
    font-size: 29px; line-height: 36px; font-weight: 400; color: var(--ink);
  }
  .tagline strong { font-weight: 700; }
  .lede {
    position: absolute; left: 29px; top: 400px;
    font-size: 13.5px; line-height: 25px; color: var(--ink);
  }
  .lede strong { font-weight: 700; }
  .call-pill {
    position: absolute; left: 0; top: 464px; width: 472px; height: 52px;
    background: var(--red); border-radius: 0 26px 26px 0;
    color: #fff; font-size: 33px; font-weight: 600;
    display: flex; align-items: center; padding-left: 36px; letter-spacing: .01em;
  }
  .front-url { position: absolute; left: 29px; top: 533px; font-size: 13px; }

  .info-band {
    position: absolute; left: 0; top: 35px; width: 722px; height: 48px;
    background: var(--red); color: #fff; padding: 6px 0 0 26px;
    font-size: 15px; line-height: 20px;
  }
  .info-band strong { font-weight: 700; display: block; }
  .postage {
    position: absolute; left: 546px; top: 12px; width: 167px; height: 161px;
    background: #fff; border: 1px solid #9a9a9a;
    font-family: "Arimo", Arial, sans-serif; font-size: 19px; line-height: 24px;
    text-align: center; padding-top: 52px;
  }
  .contact { position: absolute; left: 24px; top: 102px; font-family: "Arimo", Arial, sans-serif; }
  .contact .call-label { display: flex; align-items: center; gap: 6px; color: var(--red); font-size: 24px; font-weight: 700; }
  .contact .phone { font-size: 26px; font-weight: 700; margin: 0 0 6px 44px; line-height: 30px; }
  .contact .address { font-size: 15px; font-weight: 700; line-height: 25px; font-family: "Open Sans", Arial, sans-serif; }
  .contact .url { font-size: 17.5px; font-weight: 700; color: var(--red); font-family: "Open Sans", Arial, sans-serif; }
  .portrait {
    position: absolute; left: 23px; top: 248px; width: 115px; height: 124px;
    border: 2px solid #333; border-radius: 6px;
    background: linear-gradient(180deg, var(--photo-light), var(--photo-dark));
  }
  .signature { position: absolute; left: 23px; top: 382px; font-size: 16.5px; line-height: 23px; }
  .signature .doctor { color: var(--red); font-weight: 700; }
  .address-area { position: absolute; left: 468px; top: 215px; font-family: "Arimo", Arial, sans-serif; font-size: 19px; }
  .address-lines { position: absolute; left: 389px; top: 0; }
  .address-lines span { position: absolute; left: 0; width: 289px; height: 1px; background: var(--grey-line); }
  .brand-back {
    position: absolute; right: 16px; top: 498px;
    font-size: 13px; font-weight: 600; color: var(--red);
    display: flex; align-items: center; gap: 8px;
  }
  .brand-back .dot { width: 12px; height: 12px; border-radius: 50%; background: var(--red); }
</style>
</head>
<body>

<section class="card card--front">
  <svg class="front-art" width="722" height="554" viewBox="0 0 722 554">
    <defs>
      <linearGradient id="labPhoto" x1="0" y1="0" x2="1" y2="1">
        <stop offset="0" stop-color="#f2f2f2"/>
        <stop offset="0.6" stop-color="#bdbdbd"/>
        <stop offset="1" stop-color="#e4e4e4"/>
      </linearGradient>
    </defs>
    <polygon points="452,0 722,0 722,554 702,554 374,190" fill="url(#labPhoto)" role="img" aria-label="Photo of a pathologist looking into a microscope"/>
    <polygon points="352,190 374,190 702,554 678,554" fill="var(--red)"/>
    <polygon points="538,0 576,0 722,162 722,206" fill="var(--red)"/>
  </svg>

  <div class="brand-front"><span class="dot"></span>Corvane Skin &amp; Tissue Pathology</div>

  <h1 class="service-title">DERMATOPATHOLOGY<br>CONSULTATION<br>SERVICES</h1>
  <h2 class="tagline">LIKE HAVING A<br>DERMATOPATHOLOGIST<br><strong>IN YOUR OFFICE</strong></h2>
  <p class="lede">MeetLoop-based, online clinico-pathologic correlation to clarify difficult cases.<br>
    Dedicated to the power of <strong>Clinico- Pathologic Correlation (CPC).</strong></p>
  <div class="call-pill">CALL US : 800.555.0172</div>
  <p class="front-url">www.tissuereviewdesk.example</p>
</section>

<section class="card card--back">
  <div class="info-band">TO FIND OUT MORE ABOUT OUR<strong>DERMATOPATHOLOGY CONSULTATION SERVICES</strong></div>
  <div class="postage">Postage<br>Area</div>

  <div class="contact">
    <div class="call-label">
      <svg width="36" height="36" viewBox="0 0 36 36" aria-hidden="true">
        <circle cx="18" cy="18" r="17" fill="#222"/>
        <path d="M12 9c1.5-1 2.5-.5 3.2.8l1.4 2.8c.5 1 .3 1.9-.6 2.5l-1.2.8c.9 2.3 2.6 4.2 4.6 5.4l1-1.1c.7-.8 1.6-.9 2.5-.3l2.7 1.7c1.2.8 1.5 1.8.6 3.2-1 1.6-2.7 2.5-4.8 1.7-4.8-1.8-8.7-5.8-10.3-10.8-.6-2.3.2-5.7.9-6.7z" fill="#fff"/>
      </svg>
      Call Us
    </div>
    <div class="phone">800.555.0172</div>
    <p class="address">1480 Marlow Crest Ave. Suite 204,<br>Harbor Point, CA 90000</p>
    <p class="url">www.tissuereviewdesk.example</p>
  </div>

  <div class="portrait" role="img" aria-label="Portrait photo of the dermatopathologist"></div>

  <p class="signature">Corvane Skin &amp; Tissue<br>Pathology, Inc.<br><span class="doctor">Dana R. Ellison, M.D., Dermatopathologist</span></p>

  <p class="address-area">AddressArea</p>
  <div class="address-lines">
    <span style="top:296px"></span>
    <span style="top:328px"></span>
    <span style="top:359px"></span>
    <span style="top:390px"></span>
  </div>

  <div class="brand-back"><span class="dot"></span>Corvane Skin &amp; Tissue Pathology</div>
</section>

</body>
</html>
```